RKTA - Stewardship Website

We need a web design for our stewardship ministry. You can see what we have now: http://projects.tovask.org/

We need a new design and a total change of the website.

Industry/Entity Type

Ministry

```html
<!DOCTYPE html>
<html lang="en">
<head>
<meta charset="utf-8">
<title>RKTA – Contact Us</title>
<link rel="stylesheet" href="https://fonts.googleapis.com/css2?family=PT+Sans:ital,wght@0,400;0,700;1,400;1,700&family=Oswald:wght@500&display=swap">
<style>
:root{
  --header-bg:#eef2f6;
  --green-top:#8ccc2c;
  --green-bottom:#5e9a12;
  --green-text:#4f8a10;
  --navy:#0a4a85;
  --navy-dark:#063a6c;
  --sky:#bcdcf4;
  --ink:#111;
  --muted:#444;
  --field:#efefef;
  --field-border:#cfcfcf;
  --rule:#c9c9c9;
}
*{box-sizing:border-box;margin:0;padding:0}
html,body{width:1200px;height:1152px;overflow:hidden}
body{position:relative;background:#fff;font-family:"PT Sans",Arial,sans-serif;color:var(--ink)}
.abs{position:absolute}

.site-header{left:0;top:0;width:1200px;height:130px;background:var(--header-bg)}
.brand{left:166px;top:24px;display:flex;align-items:center;gap:12px}
.brand-mark{width:78px;height:78px;border-radius:50%;background:var(--navy)}
.brand-name{font-size:19px;font-weight:700;color:var(--navy);line-height:1.15;width:170px}
.tagline{left:475px;top:68px;font-size:21px;font-style:italic;font-weight:700;color:#222}
.top-contact{left:763px;top:16px;font-size:15px;line-height:21px;color:#111}
.top-contact b{color:var(--green-text)}
.top-contact .row{display:flex;align-items:center;gap:7px}
.search-label{left:765px;top:75px;font-size:15px;color:var(--navy)}
.search-box{left:822px;top:67px;width:216px;height:33px;border:1px solid #cfd6dd;border-radius:17px;background:#fff;display:flex;align-items:center;padding-left:14px;font-size:11px;color:#888;gap:9px}
.search-go{position:absolute;right:3px;top:3px;width:26px;height:26px;border-radius:50%;background:var(--navy);color:#fff;font-size:10px;font-weight:700;display:flex;align-items:center;justify-content:center}

.nav-band{left:0;top:130px;width:1200px;height:92px;background:linear-gradient(var(--green-top),var(--green-bottom))}
.blue-band{left:0;top:222px;width:1200px;height:31px;background:var(--navy)}
.main-nav{left:0;top:120px;width:1200px;height:77px}
.main-nav a{position:absolute;top:27px;font-family:"Oswald",sans-serif;font-weight:500;font-size:21px;color:#fff;text-decoration:none;letter-spacing:.2px}
.main-nav a.active{top:0;height:77px;width:119px;background:var(--navy);border-top:10px solid var(--green-top);text-align:center;padding-top:19px}

.hero-frame{left:144px;top:196px;width:912px;height:380px;background:var(--sky);border-radius:14px 14px 0 0;clip-path:polygon(0 0,100% 0,100% 40%,98.6% 100%,1.4% 100%,0 40%)}
.hero-photo{left:165px;top:219px;width:870px;height:334px;border:3px solid #fff;border-radius:12px;background:linear-gradient(120deg,#2d4b6a 0%,#1f7fc7 45%,#d9c8a0 70%,#3a2a20 100%)}
.hero-banner{left:234px;top:553px;width:734px;height:53px;background:linear-gradient(var(--navy),var(--navy-dark));clip-path:polygon(0 0,100% 0,99% 100%,1% 100%);display:flex;align-items:center;justify-content:center;color:#fff;font-weight:700;font-size:29px;letter-spacing:-.3px}
.banner-shadow{left:260px;top:606px;width:680px;height:10px;background:radial-gradient(ellipse at top,rgba(0,0,0,.22),transparent 70%)}

.breadcrumb{left:164px;top:641px;font-size:12px;color:#111}
.rule{left:163px;top:668px;width:874px;height:2px;background:var(--rule)}
.page-title{left:165px;top:681px;font-size:19px;color:var(--navy);letter-spacing:.2px}
.page-title span{color:var(--green-text)}
.dotted{left:163px;top:712px;width:874px;height:8px;background:repeating-linear-gradient(90deg,#9a9a9a 0 1px,transparent 1px 2px)}

.intro{left:162px;top:736px;width:380px;font-size:14.5px;line-height:18px}
.info{left:163px;width:260px}
.info h3{font-size:18px;color:var(--navy);font-weight:700;line-height:20px}
.info p{font-size:14px;line-height:17px}
.info p.strong{font-weight:700;letter-spacing:.4px}

.contact-form label{position:absolute;left:683px;font-size:14px;color:#222}
.field{position:absolute;left:760px;width:277px;height:31px;background:var(--field);border:2px solid var(--field-border);border-radius:14px}
.field.message{height:170px}
.submit{position:absolute;left:762px;top:1000px;width:83px;height:28px;border-radius:14px;background:linear-gradient(#1d6fc0,var(--navy-dark));color:#fff;font-size:14px;display:flex;align-items:center;justify-content:center}

.site-footer{left:0;top:1050px;width:1200px;height:102px;background:var(--header-bg);border-top:4px solid var(--green-bottom);text-align:center}
.follow{margin-top:26px;font-size:14px;display:flex;justify-content:center;align-items:center;gap:6px}
.follow i{display:inline-block;width:14px;height:14px;background:var(--navy)}
.follow i.alt{background:#4fb6e8}
.footer-links{margin-top:6px;font-size:11px;color:#333;line-height:13px}
</style>
</head>
<body>
<header class="abs site-header">
  <div class="abs brand"><div class="brand-mark"></div><div class="brand-name">Radiant Kingdom Teaching Assembly</div></div>
  <div class="abs tagline">Sharing in the Lord's Vineyard.</div>
  <div class="abs top-contact">
    <div class="row">
      <svg width="14" height="14" viewBox="0 0 14 14"><path d="M3 1l3 3-2 2c1 2 2 3 4 4l2-2 3 3-2 2C6 13 1 8 1 3z" fill="#7aa3c8"/></svg>
      <span><b>Call us at:</b> 08031245670 &nbsp;|&nbsp; 08059863214</span>
    </div>
    <div class="row">
      <svg width="14" height="14" viewBox="0 0 14 14"><rect x="1" y="3" width="12" height="8" fill="none" stroke="#7aa3c8" stroke-width="1.3"/><path d="M1 3l6 5 6-5" fill="none" stroke="#7aa3c8" stroke-width="1.3"/></svg>
      <span><b>Email:</b> &nbsp;projects@tovask.org</span>
    </div>
  </div>
  <div class="abs search-label">SEARCH</div>
  <div class="abs search-box">
    <svg width="12" height="12" viewBox="0 0 12 12"><circle cx="5" cy="5" r="3.5" fill="none" stroke="#999" stroke-width="1.5"/><path d="M8 8l3 3" stroke="#999" stroke-width="1.5"/></svg>
    enter your text here
    <span class="search-go">GO</span>
  </div>
</header>

<div class="abs nav-band"></div>
<div class="abs blue-band"></div>
<nav class="abs main-nav">
  <a style="left:330px">HOME</a>
  <a style="left:418px">ABOUT US</a>
  <a style="left:537px">OUR PROJECTS</a>
  <a style="left:690px">PARTNERS</a>
  <a class="active" style="left:800px">CONTACT US</a>
</nav>

<div class="abs hero-frame"></div>
<div class="abs hero-photo" role="img" aria-label="Photograph of children in blue and yellow shirts playing chess at a table"></div>
<div class="abs banner-shadow"></div>
<div class="abs hero-banner">DEDICATED TO ENRICHING THE LIVES OF OTHERS.</div>

<div class="abs breadcrumb">Home » Contact Us</div>
<div class="abs rule"></div>
<h1 class="abs page-title" style="font-weight:400">CONTACT <span>US</span></h1>
<div class="abs dotted"></div>

<p class="abs intro">Contact us today, to find out how you can join us to enrich the lives of others and positively impact our community.</p>
<div class="abs info" style="top:786px"><h3>Address</h3><p>24 Palm Grove Road, Eastbank<br>Harbor District</p></div>
<div class="abs info" style="top:852px"><h3>Phone</h3><p class="strong">08031245670<br>08059863214</p></div>
<div class="abs info" style="top:918px"><h3>Email</h3><p class="strong">projects@tovask.org</p></div>

<div class="contact-form">
  <label style="top:743px">Name*</label><div class="field" style="top:737px"></div>
  <label style="top:785px">Email*</label><div class="field" style="top:779px"></div>
  <label style="top:825px">Message*</label><div class="field message" style="top:821px"></div>
  <div class="submit">Submit</div>
</div>

<footer class="abs site-footer">
  <div class="follow">Follow us on: <i></i><i class="alt"></i></div>
  <div class="footer-links">Home &nbsp;--&nbsp; About Us &nbsp;--&nbsp; Our Projects &nbsp;--&nbsp; Partners &nbsp;--&nbsp; Contact Us<br>Radiant Kingdom Teaching Assembly © 2012 | Privacy Statement | Terms of Use</div>
</footer>
</body>
</html>
```